Castellano Wine label**

Hi, we need a design for a white, red and sparkling wine label. We are a small italian restaurant (Castellano) and we want to release some wines under our personal brand. The restaurant has a rustic, italian provance style with with a slight modern, clean lines look. We would like a design that represent our mission to provide as authentic Italian food as we can, something that feels that it has been brought from the heart of Italy.
https://www.castellanotrattoria.ru/

```html
<!DOCTYPE html>
<html lang="en">
<head>
<meta charset="utf-8">
<title>Castellano — Wine Label Series</title>
<link href="https://fonts.googleapis.com/css2?family=Cormorant+Garamond:ital,wght@0,400;0,600;1,600&display=swap" rel="stylesheet">
<style>
  :root {
    --backdrop: #f3f1ed;
    --amber: #e9a444;
    --amber-deep: #b9772a;
    --ink-brown: #4a2d14;
    --paper: #f7f5f0;
    --paper-edge: #e4e0d8;
    --engraving-olive: #8b8a62;
    --engraving-light: #c9c6a6;
    --engraving-amber: #a87430;
    --crimson: #9b2548;
    --teal: #2a8f9c;
    --gold: #c99a3c;
    --charcoal: #2b2b2b;
  }
  * { box-sizing: border-box; margin: 0; padding: 0; }
  html, body { width: 1200px; height: 746px; overflow: hidden; }
  body {
    background: var(--backdrop);
    font-family: "Cormorant Garamond", "Times New Roman", serif;
    position: relative;
  }
  .label {
    position: absolute;
    top: 150px;
    width: 290px;
    height: 440px;
    box-shadow: 0 6px 18px rgba(0,0,0,0.12);
  }

  /* Label one — amber classic */
  .label--classic { left: 90px; background: var(--amber); }
  .label--classic .frame {
    position: absolute; inset: 10px;
    border: 1.5px solid var(--ink-brown);
  }
  .label--classic .scene {
    position: absolute; left: 18px; right: 18px; top: 18px; height: 110px;
    background: linear-gradient(180deg, var(--amber) 0%, #d89a45 45%, var(--engraving-amber) 100%);
  }
  .label--classic .name-band {
    position: absolute; left: -14px; right: -14px; top: 122px; height: 58px;
    background: var(--paper);
    display: flex; align-items: center; padding-left: 40px;
  }
  .brand-name {
    font-family: "Cormorant Garamond", "Times New Roman", serif;
    font-weight: 600;
    color: var(--charcoal);
    letter-spacing: 0.12em;
    text-transform: lowercase;
  }
  .label--classic .brand-name { font-size: 34px; }
  .label--classic .tagline {
    position: absolute; left: 10px; right: 10px; top: 200px;
    border-top: 1.5px solid var(--ink-brown);
    border-bottom: 1.5px solid var(--ink-brown);
    text-align: center; padding: 4px 0 2px;
    font-size: 29px; font-weight: 400; color: var(--ink-brown); letter-spacing: 0.06em;
  }
  .label--classic .monogram {
    position: absolute; left: 115px; top: 258px; width: 60px; height: 70px;
    background: linear-gradient(180deg, var(--amber-deep), #c88a38);
    opacity: 0.6;
  }
  .label--classic .descriptor {
    position: absolute; left: 0; right: 0; top: 348px; text-align: center;
    color: var(--ink-brown);
  }
  .descriptor .kind { font-size: 21px; letter-spacing: 0.08em; display: block; text-transform: uppercase; }
  .descriptor .wine { font-size: 30px; font-style: italic; font-weight: 600; display: block; line-height: 1; }

  /* Label two — vertical name */
  .label--vertical { left: 455px; background: var(--paper); border: 1px solid var(--paper-edge); }
  .label--vertical .scene {
    position: absolute; left: 14px; top: 18px; width: 200px; height: 330px;
    background: linear-gradient(160deg, #e9e8df 0%, var(--engraving-light) 40%, var(--engraving-olive) 100%);
  }
  .label--vertical .vertical-name {
    position: absolute; left: 214px; top: 18px; width: 60px; height: 330px;
    display: flex; align-items: center; justify-content: center;
  }
  .label--vertical .vertical-name .brand-name {
    display: block; transform: rotate(90deg); white-space: nowrap; font-size: 44px;
  }
  .label--vertical .descriptor {
    position: absolute; left: 0; right: 0; bottom: 26px; text-align: center;
    font-size: 23px; letter-spacing: 0.06em; color: var(--crimson); text-transform: uppercase;
  }

  /* Label three — vintage */
  .label--vintage { left: 820px; background: var(--paper); border: 1px solid var(--paper-edge); }
  .label--vintage .scene {
    position: absolute; left: 40px; right: 40px; top: 28px; height: 160px;
    border-radius: 46% 46% 40% 40% / 30% 30% 22% 22%;
    background: radial-gradient(ellipse at 50% 45%, #d8d5b7 0%, var(--engraving-light) 45%, var(--engraving-olive) 100%);
  }
  .label--vintage .name-line {
    position: absolute; left: 0; right: 0; top: 218px; text-align: center;
  }
  .label--vintage .brand-name { font-size: 36px; }
  .label--vintage .rule {
    position: absolute; left: 36px; right: 22px; top: 274px; height: 2px;
    background: linear-gradient(90deg, rgba(201,154,60,0.2), var(--gold) 30%, var(--gold));
  }
  .label--vintage .descriptor { position: absolute; left: 0; right: 0; top: 302px; text-align: center; }
  .label--vintage .kind { color: var(--teal); font-size: 22px; }
  .label--vintage .wine { color: var(--crimson); font-size: 32px; }
  .label--vintage .vintage-year {
    display: block; margin-top: 12px; color: var(--teal); font-size: 22px; font-weight: 600; letter-spacing: 0.06em;
  }
</style>
</head>
<body>
  <section class="label label--classic">
    <div class="frame"></div>
    <div class="scene" role="img" aria-label="Engraved Tuscan hillside village with cypress trees and vineyard rows"></div>
    <div class="name-band"><span class="brand-name">castellano</span></div>
    <div class="tagline">REAL TASTE</div>
    <div class="monogram" role="img" aria-label="Ornamental script initial"></div>
    <div class="descriptor">
      <span class="kind">Italian Fine</span>
      <span class="wine">wine</span>
    </div>
  </section>

  <section class="label label--vertical">
    <div class="scene" role="img" aria-label="Pencil engraving of rolling vineyards with a cypress and farmhouse"></div>
    <div class="vertical-name"><span class="brand-name">castellano</span></div>
    <div class="descriptor">Italian Wine</div>
  </section>

  <section class="label label--vintage">
    <div class="scene" role="img" aria-label="Engraved vineyard landscape with a villa on the hill"></div>
    <div class="name-line"><span class="brand-name">castellano</span></div>
    <div class="rule"></div>
    <div class="descriptor">
      <span class="kind">Italian Fine</span>
      <span class="wine">wine</span>
      <span class="vintage-year">2020</span>
    </div>
  </section>
</body>
</html>
```